Direct Mail Postcard- Lighting Company

Our task is to send a postcard directly to houses surrounding where our company has done work. My goal is to position ourselves as the go to outdoor lighting partner for their neighborhood.
Trusted Lighting Design & Maintenance Your neighbor chose us to enhance and maintain their home's beauty and security. Now, we're offering our top-tier services to the entire neighborhood.
Please emphasize our:
Maintenance Excellence:
Regular system check-ups
Prompt repair and replacement
Upgrades to the latest technology
Less emphasis on:
Our Services:
High-Quality Landscape & Architectural Lighting
Reliable Permanent Lighting Solutions
Call us today and take advantage of our 25% discount (limited time offer)
For more details or to schedule a consultation, visit brightvane-mo.com or call .
*Need to be able to tweak this for future campaigns. Quickly edit verbiage for future marketing campaigns. I.e. a file that can be edited through Canva
*Inspiration photo file (Yard Glow Horizons)
*Would like to incorporate the before and after png
Call: (816) 555-0193
brightvane-mo.com
Updates
I attached a new before and after photo. Please create a design implementing this
Look and feel
Each slider illustrates characteristics of the customer's brand and the style your logo design should communicate.

```html
<!DOCTYPE html>
<html lang="en">
<head>
<meta charset="utf-8">
<title>Brightvane Lighting – Neighborhood Postcard</title>
<link href="https://fonts.googleapis.com/css2?family=Cinzel:wght@400;500&family=Montserrat:wght@300;400;500;600;700&display=swap" rel="stylesheet">
<style>
  :root {
    --navy: #2f3b4b;
    --gold: #b89b52;
    --paper: #ffffff;
    --backdrop: #9ea4a6;
    --ink: #2b2f36;
    --shadow: rgba(0,0,0,0.28);
  }
  * { box-sizing: border-box; margin: 0; padding: 0; }
  html, body { width: 1200px; height: 2271px; overflow: hidden; }
  body { background: var(--backdrop); font-family: 'Montserrat', sans-serif; color: var(--ink); position: relative; }

  .postcard { position: absolute; left: 100px; width: 1000px; height: 670px; background: var(--paper); overflow: hidden; box-shadow: 0 4px 12px var(--shadow); }
  .postcard--front { top: 443px; }
  .postcard--back { top: 1158px; }

  .corner-tab { position: absolute; left: 0; top: 0; width: 62px; height: 58px; background: var(--gold); clip-path: polygon(0 0, 100% 0, 0 100%); }

  .oval-art { position: absolute; left: 0; top: 0; }

  .centered { position: absolute; text-align: center; }
  .dotted-rule { position: absolute; border-top: 2px dotted var(--navy); height: 0; }

  /* Front */
  .brand { left: 577px; width: 360px; top: 52px; font-weight: 300; color: var(--ink); }
  .brand__name { font-size: 50px; letter-spacing: 4px; line-height: 1; }
  .brand__sub { font-size: 32px; letter-spacing: 22px; line-height: 1; margin-top: 14px; padding-left: 22px; }
  .headline { left: 550px; width: 420px; top: 234px; font-family: 'Cinzel', serif; font-weight: 400; font-size: 39px; line-height: 44px; color: var(--ink); white-space: nowrap; }
  .intro { left: 550px; width: 420px; top: 449px; font-size: 15.5px; line-height: 19px; font-weight: 400; white-space: nowrap; }
  .intro p + p { margin-top: 18px; }
  .web-pill { position: absolute; left: 577px; top: 580px; width: 362px; height: 39px; border-radius: 7px; background: var(--gold); color: #fff; font-weight: 600; font-size: 20px; letter-spacing: 0.5px; display: flex; align-items: center; justify-content: center; }

  /* Back */
  .section-title { font-family: 'Cinzel', serif; font-weight: 400; font-size: 22px; letter-spacing: 1px; color: var(--ink); white-space: nowrap; }
  .service-item { font-size: 14px; line-height: 18.5px; text-transform: uppercase; color: var(--ink); width: 130px; white-space: nowrap; }
  .gold-divider { position: absolute; width: 2px; background: var(--gold); }

  .proof-photo { position: absolute; top: 400px; height: 138px; width: 226px; }
  .proof-photo--before { left: 36px; background: linear-gradient(160deg, #2a2620, #0d0c0b 60%, #1a1814); }
  .proof-photo--after { left: 274px; background: linear-gradient(170deg, #3b3a38 0%, #8d8779 45%, #2a2926 100%); }
  .proof-photo__label { position: absolute; left: 9px; bottom: 7px; color: #fff; font-size: 11px; font-weight: 500; }

  .offer-text { left: 520px; width: 420px; top: 390px; font-size: 19px; line-height: 26px; font-weight: 500; color: var(--navy); text-transform: uppercase; white-space: nowrap; }
  .discount-box { position: absolute; left: 541px; top: 479px; width: 378px; height: 53px; border: 2px dashed var(--gold); color: var(--gold); font-family: 'Cinzel', serif; font-weight: 500; font-size: 37px; line-height: 1; display: flex; align-items: center; justify-content: center; }

  .details-band { position: absolute; left: 0; top: 549px; width: 100%; height: 46px; background: var(--gold); color: #fff; font-family: 'Cinzel', serif; font-size: 20px; letter-spacing: 0.5px; display: flex; align-items: center; justify-content: center; }
  .contact-band { position: absolute; left: 0; top: 595px; width: 100%; height: 75px; background: var(--navy); color: #fff; display: flex; align-items: center; justify-content: center; gap: 50px; }
  .contact-item { display: flex; align-items: center; gap: 10px; font-weight: 700; }
  .contact-item--phone { font-size: 27px; }
  .contact-item--web { font-size: 20px; font-weight: 600; }
</style>
</head>
<body>

<section class="postcard postcard--front">
  <div class="corner-tab"></div>
  <svg class="oval-art" width="560" height="670" viewBox="0 0 560 670">
    <defs>
      <linearGradient id="garden" x1="0" y1="0" x2="0" y2="1">
        <stop offset="0" stop-color="#2f3b22"/>
        <stop offset="0.45" stop-color="#6b3d24"/>
        <stop offset="0.75" stop-color="#3e4a27"/>
        <stop offset="1" stop-color="#4f6b2a"/>
      </linearGradient>
    </defs>
    <ellipse cx="287" cy="335" rx="233" ry="299" fill="var(--navy)"/>
    <ellipse cx="293" cy="330" rx="203" ry="272" fill="url(#garden)" role="img" aria-label="Photo of a brick home at dusk with landscape lights glowing along a stone garden wall"/>
  </svg>

  <div class="centered brand">
    <div class="brand__name">BRIGHTVANE</div>
    <div class="brand__sub">LIGHTING</div>
  </div>

  <div class="dotted-rule" style="left:577px; top:219px; width:360px;"></div>
  <h1 class="centered headline">ELEVATE YOUR<br>OUTDOOR SPACES<br>WITH PREMIUM<br>LIGHTING</h1>
  <div class="dotted-rule" style="left:577px; top:423px; width:360px;"></div>

  <div class="centered intro">
    <p>Trusted Lighting Design &amp; Maintenance<br>Your neighbor chose us to enhance and<br>maintain their home's beauty &amp; security.</p>
    <p>Now, we're offering our top-tier services<br>to the entire neighborhood.</p>
  </div>

  <div class="web-pill">www.brightvane-mo.com</div>
</section>

<section class="postcard postcard--back">
  <div class="corner-tab"></div>

  <svg class="oval-art" width="1000" height="670" viewBox="0 0 1000 670">
    <defs>
      <linearGradient id="entry" x1="0" y1="0" x2="0" y2="1">
        <stop offset="0" stop-color="#3d5a8c"/>
        <stop offset="0.4" stop-color="#8a7a66"/>
        <stop offset="0.75" stop-color="#5a5248"/>
        <stop offset="1" stop-color="#3f5a2a"/>
      </linearGradient>
    </defs>
    <ellipse cx="731" cy="141" rx="233" ry="233" fill="var(--navy)"/>
    <ellipse cx="731" cy="123" rx="203" ry="222" fill="url(#entry)" role="img" aria-label="Photo of a columned home entrance lit by path and uplights at twilight"/>
  </svg>

  <div class="dotted-rule" style="left:89px; top:35px; width:357px;"></div>
  <h2 class="centered section-title" style="left:89px; width:357px; top:46px;">OUR SERVICES</h2>
  <div class="dotted-rule" style="left:89px; top:77px; width:357px;"></div>

  <div class="centered service-item" style="left:68px; top:113px;">High-Quality<br>Landscape &amp;<br>Architectural<br>Lighting</div>
  <div class="gold-divider" style="left:214px; top:93px; height:97px;"></div>
  <div class="centered service-item" style="left:219px; top:113px;">Reliable<br>Permanent<br>Lighting<br>Solutions</div>
  <div class="gold-divider" style="left:351px; top:93px; height:97px;"></div>
  <div class="centered service-item" style="left:353px; top:113px;">Reliable<br>Permanent<br>Lighting<br>Solutions</div>

  <div class="dotted-rule" style="left:77px; top:231px; width:359px;"></div>
  <h2 class="centered section-title" style="left:77px; width:359px; top:239px;">MAINTENANCE EXCELLENCE</h2>
  <div class="dotted-rule" style="left:77px; top:271px; width:359px;"></div>

  <div class="centered service-item" style="left:56px; top:315px;">Regular<br>System<br>Check-Ups</div>
  <div class="gold-divider" style="left:203px; top:288px; height:94px;"></div>
  <div class="centered service-item" style="left:207px; top:315px;">Prompt<br>Repair and<br>Replacement</div>
  <div class="gold-divider" style="left:340px; top:288px; height:94px;"></div>
  <div class="centered service-item" style="left:341px; top:315px;">Upgrades to<br>the Latest<br>Technology</div>

  <div class="proof-photo proof-photo--before" role="img" aria-label="Before photo of a dark, unlit home at night">
    <span class="proof-photo__label">BEFORE</span>
  </div>
  <div class="proof-photo proof-photo--after" role="img" aria-label="After photo of the same home with facade and tree lighting">
    <span class="proof-photo__label">AFTER</span>
  </div>

  <p class="centered offer-text">Reach out today<br>to schedule your appointment<br>&amp; take advantage of our</p>
  <div class="discount-box">25% DISCOUNT</div>

  <div class="details-band">FOR MORE DETAILS OR TO SCHEDULE A CONSULTATION</div>
  <div class="contact-band">
    <div class="contact-item contact-item--phone">
      <svg width="22" height="22" viewBox="0 0 24 24" aria-hidden="true"><path fill="var(--gold)" d="M6.6 10.8a15.1 15.1 0 0 0 6.6 6.6l2.2-2.2a1 1 0 0 1 1-.25 11.4 11.4 0 0 0 3.6.57 1 1 0 0 1 1 1V20a1 1 0 0 1-1 1A17 17 0 0 1 3 4a1 1 0 0 1 1-1h3.5a1 1 0 0 1 1 1c0 1.25.2 2.450.57 3.57a1 1 0 0 1-.25 1z"/></svg>
      <span>(816) 555-0193</span>
    </div>
    <div class="contact-item contact-item--web">
      <svg width="20" height="20" viewBox="0 0 24 24" aria-hidden="true" fill="none" stroke="var(--gold)" stroke-width="2"><circle cx="12" cy="12" r="10"/><path d="M2 12h20M12 2c3 3 3 17 0 20M12 2c-3 3-3 17 0 20"/></svg>
      <span>www.brightvane-mo.com</span>
    </div>
  </div>
</section>

</body>
</html>
```